New Business Card Design For Re-Branded Company (New Logo)

We recently switched our DBA and had a new logo designed. We now need new business cards made around our new logo. We would like to stick with the color scheme in our logo: White, Orange, and Blue. We want to see original bold designs that reflect our position in the solar energy sector but we prefer simple over complicated.

We are curious about vertical designs so if you can translate your design onto a vertical layout we would be open to look at it. We especially like a few designs we have seen on here that are vertical with a black or very dark gray background. They have our logo on one side and then the normal vertical business card on the other side.

I have included a screenshot of one of the samples we like, labeled sample.jpg and a file we were given as an example of our logo on a dark background.

At the same time we are satisfied to stay with what we have always had in a horizontal format. If it's not a lot of extra work for you, designs that are submitted in both horizontal and vertical formats will be greatly appreciated.

Please submit your original, bold, clean designs for consideration. Contact us with any questions or comments that may arise.

Thank you and Good Luck,

KP

```html
<!DOCTYPE html>
<html lang="en">
<head>
<meta charset="utf-8">
<title>Kestrel Power – Business Cards</title>
<link href="https://fonts.googleapis.com/css2?family=Michroma&family=Montserrat:wght@400;500;600&display=swap" rel="stylesheet">
<style>
  :root {
    --stage: #e6e3de;
    --card: #232323;
    --orange: #f07f22;
    --blue: #1f87d0;
    --white: #f2f2f2;
  }
  * { box-sizing: border-box; margin: 0; padding: 0; }
  html, body { width: 1200px; height: 950px; overflow: hidden; }
  body {
    background: var(--stage);
    display: flex;
    align-items: center;
    justify-content: center;
    gap: 80px;
    font-family: "Montserrat", sans-serif;
  }
  .card {
    position: relative;
    width: 400px;
    height: 700px;
    background: var(--card);
    box-shadow: 0 10px 30px rgba(0,0,0,.25);
    color: var(--white);
  }
  .frame-outer, .frame-inner { position: absolute; pointer-events: none; }
  .frame-outer { inset: 16px; border: 2px solid var(--orange); }
  .frame-inner { inset: 24px; border: 2px solid var(--blue); }

  .brand-name {
    font-family: "Michroma", sans-serif;
    font-size: 21px;
    color: var(--orange);
    letter-spacing: 0;
    white-space: nowrap;
  }

  /* Front */
  .front { display: flex; flex-direction: column; align-items: center; text-align: center; padding: 70px 40px 0; }
  .brand { display: flex; flex-direction: column; align-items: center; gap: 16px; }
  .brand-dot { width: 40px; height: 40px; border-radius: 50%; background: var(--orange); }
  .person { margin-top: 44px; }
  .person-name { font-family: "Michroma", sans-serif; font-size: 17px; color: var(--blue); letter-spacing: 1px; white-space: nowrap; }
  .person-role { font-family: "Michroma", sans-serif; font-size: 12px; color: var(--orange); margin-top: 8px; }
  .address { margin-top: 34px; font-size: 16px; line-height: 1.5; font-style: normal; }
  .phones { margin-top: 20px; font-size: 16px; line-height: 1.6; }
  .phones .label { color: var(--blue); font-weight: 600; margin-right: 6px; }
  .online { margin-top: 20px; font-size: 16px; line-height: 1.6; }

  /* Back */
  .back { overflow: hidden; }
  .back-mark {
    position: absolute;
    left: 50%;
    top: 250px;
    transform: translate(-50%, -50%);
  }
  .back-brand {
    position: absolute;
    left: 40px; right: 40px;
    bottom: 90px;
    text-align: center;
  }
  .back-web {
    margin-top: 12px;
    font-size: 14px;
    letter-spacing: 5px;
    color: var(--white);
    white-space: nowrap;
  }
</style>
</head>
<body>
  <article class="card front">
    <div class="frame-outer"></div>
    <div class="frame-inner"></div>
    <div class="brand">
      <span class="brand-dot"></span>
      <span class="brand-name">KESTREL POWER</span>
    </div>
    <div class="person">
      <p class="person-name">DANA MORROW</p>
      <p class="person-role">CEO / FOUNDER</p>
    </div>
    <address class="address">
      4120 Willow Crest Road<br>Fairbanks, Alaska 99701
    </address>
    <div class="phones">
      <p><span class="label">P:</span>555 210 4471</p>
      <p><span class="label">M:</span>555 382 0916</p>
      <p><span class="label">F:</span>555 774 2053</p>
    </div>
    <div class="online">
      <p>hello@kestrelpower.com</p>
      <p>www.kestrelpower.com</p>
    </div>
  </article>

  <article class="card back">
    <div class="frame-outer"></div>
    <div class="frame-inner"></div>
    <svg class="back-mark" width="300" height="300" viewBox="0 0 300 300" aria-hidden="true">
      <circle cx="150" cy="150" r="130" fill="none" stroke="var(--orange)" stroke-width="26"/>
    </svg>
    <div class="back-brand">
      <p class="brand-name">KESTREL POWER</p>
      <p class="back-web">www.kestrelpower.com</p>
    </div>
  </article>
</body>
</html>
```